Masonry and Landscaping Construction company business card

Looking for a business card design for a construction company named Ferrano Construction. It is an italian-american family business that specializes in custom stone work, patios, walkways, driveways, steps, outdoor kitchens, concrete, waterproofing, power wash, landscaping and more. Our colors are mostly red and white with some black. We're looking for a bold design. we also like to incorporate a picture of my family's hometown somewhere in it.
Target Market(s)
Luxury home owners
Industry/Entity Type
Construction
Contact Information for Business Card
Details includes should be bullet points mentioning the services provided. Custom Stone Work, Outdoor Kitchens, Fire Pits, Patios, Walkways, Steps, Concrete, Waterproofing, powerwash and landscaping
Requirements
Must have
- Would like a spot on the card for co-owners names, numbers and email to be listed also looking to add the QR code for an instagram page
Nice to have
- would like something bold, based around the colors red and white with black outlines or details

```html
<!DOCTYPE html>
<html lang="en">
<head>
<meta charset="utf-8">
<title>Ferrano Construction – Business Card</title>
<link rel="stylesheet" href="https://fonts.googleapis.com/css2?family=Barlow+Condensed:wght@600;700&family=Roboto:wght@400;500;700&display=swap">
<style>
  :root {
    --stage: #3b3b3d;
    --card-white: #ffffff;
    --brand-red: #d7192a;
    --ink: #2b2b2b;
    --muted: #6a6a6a;
    --charcoal: #3a3a3c;
    --band-green: #16d65e;
    --band-ink: #0f3d1c;
  }
  * { box-sizing: border-box; margin: 0; padding: 0; }
  html, body { width: 1200px; height: 689px; overflow: hidden; }
  body {
    background: var(--stage);
    font-family: "Roboto", sans-serif;
    position: relative;
  }
  .card {
    position: absolute;
    width: 520px;
    height: 300px;
    border-radius: 18px;
    overflow: hidden;
    box-shadow: 0 14px 30px rgba(0,0,0,.45);
  }

  /* Front: hometown photo side */
  .card-front { left: 45px; top: 80px; }
  .hometown-photo {
    position: absolute; inset: 0;
    background: linear-gradient(180deg, #c9d3dc 0%, #aebfca 22%, #6f8a5a 45%, #587a44 62%, #a48f74 80%, #8f7a60 100%);
  }
  .front-brand {
    position: absolute; right: 30px; top: 34px;
    display: flex; align-items: center; gap: 10px;
    background: rgba(255,255,255,.92);
    padding: 12px 18px; border-radius: 6px;
  }
  .brand-square { width: 18px; height: 18px; background: var(--brand-red); flex: none; }
  .brand-name {
    font-family: "Roboto", sans-serif; font-weight: 700;
    font-size: 22px; color: var(--ink); letter-spacing: .5px;
    white-space: nowrap;
  }
  .services-band {
    position: absolute; left: 0; right: 0; bottom: 44px;
    background: var(--band-green);
    padding: 10px 10px;
    color: var(--band-ink);
    font-size: 13.5px; line-height: 1.5; text-align: center;
  }
  .services-band p { white-space: nowrap; }
  .services-band .dot { color: var(--brand-red); padding: 0 4px; }

  /* Back: contact side */
  .card-back { left: 635px; top: 300px; background: var(--card-white); }
  .back-brand {
    position: absolute; left: 26px; top: 112px;
    display: flex; align-items: center; gap: 9px;
  }
  .back-brand .brand-name { font-size: 20px; letter-spacing: .2px; }
  .divider {
    position: absolute; left: 282px; top: 28px;
    width: 1px; height: 175px;
    background: linear-gradient(180deg, transparent, #bdbdbd 25%, #bdbdbd 75%, transparent);
  }
  .contact {
    position: absolute; left: 298px; top: 30px; width: 212px;
    color: var(--ink);
  }
  .person-name {
    font-family: "Barlow Condensed", sans-serif; font-weight: 700;
    font-size: 26px; color: var(--brand-red); line-height: 1;
  }
  .person-role { font-size: 12px; color: var(--muted); margin-top: 2px; }
  .address { font-size: 12.5px; line-height: 1.35; margin-top: 12px; }
  .contact-list { list-style: none; margin-top: 10px; font-size: 12.5px; line-height: 1.5; }
  .contact-list li { display: flex; align-items: center; gap: 7px; white-space: nowrap; }
  .contact-list svg { width: 11px; height: 11px; flex: none; }
  .footer-band { position: absolute; left: 0; bottom: 0; width: 520px; height: 92px; }
  .website {
    position: absolute; right: 22px; bottom: 30px;
    color: #fff; font-size: 13px; letter-spacing: .3px;
  }
</style>
</head>
<body>

  <section class="card card-front">
    <div class="hometown-photo" role="img" aria-label="Photo of the family's Italian hometown: stone church bell tower and old town houses beneath green mountains and a cloudy sky"></div>
    <div class="front-brand">
      <span class="brand-square"></span>
      <span class="brand-name">Ferrano Construction</span>
    </div>
    <div class="services-band">
      <p>Custom Stone Work<span class="dot">•</span>Outdoor Kitchens<span class="dot">•</span>Fire Pits<span class="dot">•</span>Patios<span class="dot">•</span>Walkways</p>
      <p>Steps<span class="dot">•</span>Concrete<span class="dot">•</span>Waterproofing<span class="dot">•</span>Powerwash &amp; Landscaping</p>
    </div>
  </section>

  <section class="card card-back">
    <div class="back-brand">
      <span class="brand-square"></span>
      <span class="brand-name">Ferrano Construction</span>
    </div>
    <div class="divider"></div>
    <div class="contact">
      <h1 class="person-name">MARCO BELLINI</h1>
      <p class="person-role">President</p>
      <p class="address">412 Alder Ridge Road<br>Fairview, Canada 52190</p>
      <ul class="contact-list">
        <li>
          <svg viewBox="0 0 12 12"><path d="M2.5 1l2 2.5-1 1.3c.7 1.5 1.8 2.6 3.2 3.2l1.3-1 2.5 2-1 1.5C5.5 10.5 1.5 6.5 1 2z" fill="#d7192a"/></svg>
          555-210-4817
        </li>
        <li>
          <svg viewBox="0 0 12 12"><rect x="3" y="0.8" width="6" height="10.4" rx="1" fill="none" stroke="#d7192a" stroke-width="1.2"/></svg>
          555-382-9064
        </li>
        <li>
          <svg viewBox="0 0 12 12"><rect x="0.8" y="2.5" width="10.4" height="7" fill="#d7192a"/><path d="M1 3l5 3.5L11 3" fill="none" stroke="#fff" stroke-width="1"/></svg>
          info@ferranoconstruction.com
        </li>
      </ul>
    </div>
    <svg class="footer-band" viewBox="0 0 520 92" aria-hidden="true">
      <polygon points="0,80 250,80 290,40 520,40 520,92 0,92" fill="#3a3a3c"/>
      <polygon points="0,72 246,72 286,32 296,32 256,76 0,76" fill="#d7192a"/>
    </svg>
    <p class="website">www.ferranoconstruction.com</p>
  </section>

</body>
</html>
```